Rent Kiosks and Tablets

Website for rental kiosks and tablets following the model / style http://www.quellstander.com/. May be the same, with changes in visual identity.
The site should also have an online order system like an e-commerce, which allows payment by credit card and ticket.

The company is called Bolumexa.com and feel free to create/suggest styles of names design.

Target Market(s)

Events, trade shows, marketing companies.

Industry/Entity Type

Credit Card

Font styles to use
Sans Serif

Colors

Designer to choose colors to be used in the design.

```html
<!DOCTYPE html>
<html lang="en">
<head>
<meta charset="utf-8">
<title>Bolumexa.com — Kiosk &amp; Tablet Rentals</title>
<link href="https://fonts.googleapis.com/css2?family=Lato:wght@300;400;700&family=Raleway:wght@300;400;600;700&display=swap" rel="stylesheet">
<style>
:root{
  --accent:#e2633f;
  --accent-strong:#e0402a;
  --ink:#2b2b2b;
  --muted:#7a7a7a;
  --rule:#e3e3e3;
  --light:#eeeeee;
  --dark:#2f2f2f;
  --topbar:#1c1c1c;
  --nav:#232323;
  --white:#ffffff;
}
*{box-sizing:border-box;margin:0;padding:0}
html,body{width:1200px;height:3097px;overflow:hidden}
body{font-family:'Lato',sans-serif;color:var(--ink);background:var(--white);position:relative}
.abs{position:absolute}
section,header,footer{position:absolute;left:0;width:1200px}
.heading{font-family:'Raleway',sans-serif;font-weight:400;font-size:34px;color:var(--ink);text-align:center;width:100%}
.lead{font-size:12px;line-height:19px;color:var(--muted);text-align:center;width:820px;left:190px}
.btn{display:flex;align-items:center;justify-content:center;background:var(--accent);color:var(--white);font-size:12px;font-weight:700;letter-spacing:.5px;text-transform:uppercase;border-radius:4px;width:137px;height:42px}

/* top bar */
.topbar{top:0;height:52px;background:var(--topbar);color:#9a9a9a;font-size:11px}
.topbar .item{display:flex;align-items:center;gap:8px;top:0;height:52px}
.topbar .sep{top:0;width:1px;height:52px;background:#333}
.topbar .cart b{color:var(--accent);font-weight:700}

/* nav */
.nav{top:52px;height:62px;background:var(--nav)}
.logo{left:150px;top:14px;font-family:'Raleway',sans-serif;font-weight:600;font-size:28px;color:var(--accent)}
.menu{right:155px;top:0;height:62px;display:flex;align-items:center;gap:34px;color:var(--white);font-size:14px}

/* hero */
.hero{top:114px;height:454px;background:linear-gradient(100deg,#4a2a17 0%,#7a4a28 30%,#b07a45 55%,#6b4026 80%,#3b2517 100%)}
.hero-device{left:660px;top:30px;width:360px;height:380px;border-radius:20px;background:radial-gradient(ellipse at 50% 40%,#3a3a3a,#151515 70%);opacity:.9}
.hero-title{left:186px;top:170px;font-family:'Raleway',sans-serif;font-weight:700;font-size:38px;line-height:46px;color:var(--white)}
.arrow{top:199px;width:60px;height:60px;border-radius:50%;background:rgba(255,255,255,.85);display:flex;align-items:center;justify-content:center}

/* solutions */
.solutions{top:568px;height:614px}
.solutions .heading{top:50px}
.solutions .heading span{color:var(--accent-strong)}
.solutions .rule{left:77px;top:108px;width:1046px;height:1px;background:var(--rule)}
.solutions .lead{top:137px}
.video{left:165px;top:252px;width:437px;height:297px;background:#e6e6e6}
.video .bar{left:0;bottom:0;width:100%;height:28px;background:#1f1f1f}
.video .progress{left:0;bottom:28px;width:100%;height:5px;background:#555}
.video .progress i{display:block;width:18%;height:100%;background:#cc2a22}
.video .play{left:178px;top:110px;width:82px;height:54px;border-radius:12px;background:#222;display:flex;align-items:center;justify-content:center}
.checks{left:627px;top:258px;list-style:none}
.checks li{display:flex;align-items:center;gap:18px;height:49px;font-size:13px;color:#444}
.checks .box{width:22px;height:22px;border:2px solid var(--accent);border-radius:3px;display:flex;align-items:center;justify-content:center}
.solutions .btn{left:627px;top:510px}

/* compatible */
.compat{top:1182px;height:294px;background:var(--light)}
.compat .heading{top:30px}
.platform{top:130px;display:flex;align-items:center;gap:12px;font-family:'Lato',sans-serif;font-weight:700;font-size:26px;color:#3a3a3a}
.platform i{display:block;width:44px;height:44px;background:#9b9b9b;border-radius:4px}

/* leverage */
.leverage{top:1476px;height:336px;background:var(--dark)}
.leverage h2{left:152px;top:64px;font-family:'Raleway',sans-serif;font-weight:400;font-size:34px;line-height:40px;color:var(--white)}
.leverage p{left:152px;top:154px;width:420px;font-size:13px;line-height:17px;color:#8a8a8a}
.leverage .btn{left:152px;top:226px}
.leverage-devices{left:660px;top:46px;width:424px;height:286px;border-radius:14px;background:linear-gradient(135deg,#e9e9ea 0%,#b7b8ba 40%,#3a3b3d 70%,#1a1a1b 100%)}

/* consulting */
.consulting{top:1812px;height:413px}
.consulting h2{left:152px;top:96px;font-family:'Raleway',sans-serif;font-weight:400;font-size:34px;line-height:40px;color:var(--ink)}
.consulting p{left:152px;top:186px;width:500px;font-size:13px;line-height:17px;color:#444}
.consulting .btn{left:152px;top:309px}
.hex{width:110px;height:124px}
.hex .label{left:0;top:80px;width:110px;text-align:center;color:var(--white);font-size:11px;font-weight:700;text-transform:uppercase}

/* trusted */
.trusted{top:2225px;height:240px;background:var(--light)}
.trusted .heading{top:48px}
.partners{left:160px;top:108px;width:880px;display:flex;justify-content:space-between;align-items:center;font-family:'Lato',sans-serif;font-weight:700;font-size:19px;color:#2a2a2a}

/* blog */
.blog{top:2465px;height:573px}
.blog .heading{top:36px}
.blog .lead{top:84px}
.post{width:300px;height:125px}
.post .thumb{left:0;top:0;width:127px;height:121px;background:linear-gradient(160deg,#3b2a22,#8c3b26 50%,#1e1e1e)}
.post h3{left:135px;top:0;width:160px;font-size:14px;font-weight:400;line-height:17px;color:#222}
.post p{left:135px;top:60px;width:150px;font-size:11px;line-height:15px;color:var(--muted)}

/* footer */
.footer{top:3038px;height:59px;background:var(--topbar)}
.footer nav{left:150px;top:0;height:59px;display:flex;align-items:center;gap:20px;color:#9a9a9a;font-size:11px;text-transform:uppercase}
.social{top:18px;width:24px;height:24px;border-radius:50%;background:var(--accent)}
</style>
</head>
<body>

<header class="topbar">
  <div class="item abs" style="left:155px">
    <svg width="14" height="10" viewBox="0 0 14 10"><rect x=".5" y=".5" width="13" height="9" fill="none" stroke="#9a9a9a"/><path d="M.5 .5 7 6 13.5 .5" fill="none" stroke="#9a9a9a"/></svg>
    hello@bolumexa.com
  </div>
  <div class="item abs" style="left:335px">
    <svg width="12" height="12" viewBox="0 0 12 12"><path d="M2 1l2 0 1 3-1.5 1a7 7 0 0 0 3.5 3.5L8 7l3 1v2a1 1 0 0 1-1 1A9 9 0 0 1 1 2a1 1 0 0 1 1-1z" fill="#9a9a9a"/></svg>
    +84 900 555 010
  </div>
  <div class="sep abs" style="left:655px"></div>
  <div class="item abs" style="left:675px">
    <svg width="12" height="12" viewBox="0 0 12 12"><circle cx="5" cy="5" r="4" fill="none" stroke="#9a9a9a" stroke-width="1.5"/><path d="M8 8l3 3" stroke="#9a9a9a" stroke-width="1.5"/></svg>
    Enter your keywords
  </div>
  <div class="sep abs" style="left:815px"></div>
  <div class="item cart abs" style="left:835px">
    <svg width="14" height="12" viewBox="0 0 14 12"><path d="M0 1h2.5l2 7h7l2-5H4" fill="none" stroke="#9a9a9a" stroke-width="1.3"/><circle cx="5.5" cy="10.5" r="1" fill="#9a9a9a"/><circle cx="10.5" cy="10.5" r="1" fill="#9a9a9a"/></svg>
    Shopping Cart <b>03 items</b> for <b>$12.560</b>
  </div>
</header>

<header class="nav">
  <div class="logo abs">Bolumexa.com</div>
  <nav class="menu abs">
    <span>Services</span><span>Products</span><span>Leasing</span><span>Case Studies ▾</span><span>Company ▾</span>
  </nav>
</header>

<section class="hero" role="img" aria-label="Blurred retail shop interior with a countertop tablet kiosk on a stand">
  <div class="hero-device abs" role="img" aria-label="Black countertop tablet kiosk showing a flower on its screen"></div>
  <h1 class="hero-title abs">All-in-One Solutions<br>for Your Business</h1>
  <div class="arrow abs" style="left:89px"><svg width="16" height="22" viewBox="0 0 16 22"><path d="M12 2 3 11l9 9" fill="none" stroke="#333" stroke-width="4"/></svg></div>
  <div class="arrow abs" style="left:1046px"><svg width="16" height="22" viewBox="0 0 16 22"><path d="M4 2l9 9-9 9" fill="none" stroke="#333" stroke-width="4"/></svg></div>
</section>

<section class="solutions">
  <h2 class="heading abs">We Provide <span>Web</span> Solutions</h2>
  <div class="rule abs"></div>
  <p class="lead abs">Lorem ipsum dolor sit amet, consectetur adipiscing elit. Aliquam laoreet sodales lacinia. Curabitur ut purus tincidunt, iaculis elit a, eleifend augue. Phasellus blandit augue vel sollicitudin blandit.</p>
  <div class="video abs" role="img" aria-label="Embedded product video">
    <div class="play abs"><svg width="22" height="24" viewBox="0 0 22 24"><path d="M2 2l18 10L2 22z" fill="#fff"/></svg></div>
    <div class="progress abs"><i></i></div>
    <div class="bar abs"></div>
  </div>
  <ul class="checks abs">
    <li><span class="box"><svg width="12" height="10" viewBox="0 0 12 10"><path d="M1 5l3.5 3.5L11 1" fill="none" stroke="var(--accent)" stroke-width="2.2"/></svg></span>Aenean sollicitudin, lorem quis bibendum auctor nisi elit</li>
    <li><span class="box"><svg width="12" height="10" viewBox="0 0 12 10"><path d="M1 5l3.5 3.5L11 1" fill="none" stroke="var(--accent)" stroke-width="2.2"/></svg></span>Consequat ipsum, nec sagittis sem nibh id elit</li>
    <li><span class="box"><svg width="12" height="10" viewBox="0 0 12 10"><path d="M1 5l3.5 3.5L11 1" fill="none" stroke="var(--accent)" stroke-width="2.2"/></svg></span>Duis sed odio sit amet nibh vulputate cursus</li>
    <li><span class="box"><svg width="12" height="10" viewBox="0 0 12 10"><path d="M1 5l3.5 3.5L11 1" fill="none" stroke="var(--accent)" stroke-width="2.2"/></svg></span>Morbi accumsan ipsum velit</li>
    <li><span class="box"><svg width="12" height="10" viewBox="0 0 12 10"><path d="M1 5l3.5 3.5L11 1" fill="none" stroke="var(--accent)" stroke-width="2.2"/></svg></span>Lorem quis bibendum auctor nisi elit</li>
  </ul>
  <div class="btn abs">Read more</div>
</section>

<section class="compat">
  <h2 class="heading abs">Campatible with:</h2>
  <div class="platform abs" style="left:370px"><i></i>Fenestra OS</div>
  <div class="platform abs" style="left:575px"><i></i>Pomelo</div>
  <div class="platform abs" style="left:745px"><i></i>Robotix</div>
</section>

<section class="leverage">
  <h2 class="abs">Leverage tablets for<br>your business</h2>
  <p class="abs">We provide solutions for almost any tablet on the market, offering a wide variety of options to meet your project needs.</p>
  <div class="btn abs">Read more</div>
  <div class="leverage-devices abs" role="img" aria-label="White tablet stand and black point-of-sale tablet kiosks"></div>
</section>

<section class="consulting">
  <h2 class="abs">Consulting you<br>in the right direction.</h2>
  <p class="abs">As pioneers of integrating tablet computers into the business landscape, we strive to share our knowledge with every client to ensure you have a successful tablet kiosk deployment. Providing solutions for every industry, we are familiar with your unique integration requirements.</p>
  <div class="btn abs">Read more</div>

  <div class="hex abs" style="left:655px;top:80px">
    <svg width="110" height="124" viewBox="0 0 110 124"><polygon points="55,0 110,31 110,93 55,124 0,93 0,31" fill="var(--accent)"/><path d="M55 38 78 48 55 58 32 48z" fill="#fff"/><path d="M42 53v9c8 5 18 5 26 0v-9l-13 6z" fill="#fff"/></svg>
    <div class="label abs">Education</div>
  </div>
  <div class="hex abs" style="left:791px;top:80px">
    <svg width="110" height="124" viewBox="0 0 110 124"><polygon points="55,0 110,31 110,93 55,124 0,93 0,31" fill="var(--accent)"/><rect x="42" y="34" width="26" height="36" rx="3" fill="none" stroke="#fff" stroke-width="3"/><circle cx="55" cy="65" r="1.8" fill="#fff"/></svg>
    <div class="label abs">POS</div>
  </div>
  <div class="hex abs" style="left:928px;top:80px">
    <svg width="110" height="124" viewBox="0 0 110 124"><polygon points="55,0 110,31 110,93 55,124 0,93 0,31" fill="var(--accent)"/><circle cx="55" cy="53" r="15" fill="none" stroke="#fff" stroke-width="3"/><path d="M32 38v30M28 38v10h8V38M78 38v30" stroke="#fff" stroke-width="3" fill="none"/></svg>
    <div class="label abs">Restaurant</div>
  </div>
  <div class="hex abs" style="left:655px;top:227px">
    <svg width="110" height="124" viewBox="0 0 110 124"><polygon points="55,0 110,31 110,93 55,124 0,93 0,31" fill="var(--accent)"/><rect x="36" y="40" width="38" height="28" rx="3" fill="#fff"/><path d="M48 40v-5h14v5" fill="none" stroke="#fff" stroke-width="3"/><path d="M55 46v16M47 54h16" stroke="var(--accent)" stroke-width="4"/></svg>
    <div class="label abs">Medical</div>
  </div>
  <div class="hex abs" style="left:791px;top:227px">
    <svg width="110" height="124" viewBox="0 0 110 124"><polygon points="55,0 110,31 110,93 55,124 0,93 0,31" fill="var(--accent)"/><path d="M34 38h7l5 20h22l5-14H44" fill="none" stroke="#fff" stroke-width="3"/><circle cx="49" cy="66" r="3" fill="#fff"/><circle cx="66" cy="66" r="3" fill="#fff"/></svg>
    <div class="label abs">Retail</div>
  </div>
  <div class="hex abs" style="left:928px;top:227px">
    <svg width="110" height="124" viewBox="0 0 110 124"><polygon points="55,0 110,31 110,93 55,124 0,93 0,31" fill="var(--accent)"/><circle cx="55" cy="50" r="14" fill="none" stroke="#fff" stroke-width="3"/><path d="M47 61l-6 12 7-2 3 6 4-12M63 61l6 12-7-2-3 6-4-12" fill="#fff"/></svg>
    <div class="label abs">Non-profit</div>
  </div>
</section>

<section class="trusted">
  <h2 class="heading abs">They trusted Us</h2>
  <div class="partners abs">
    <span>Venture Weekly</span><span>The Harbor Ledger</span><span>TechPulse</span><span>Kiosk Forum</span><span>Swift Firm</span><span>Bay City Herald</span>
  </div>
</section>

<section class="blog">
  <h2 class="heading abs">Blog News</h2>
  <p class="lead abs">Lorem ipsum dolor sit amet, consectetur adipiscing elit. Aliquam laoreet sodales lacinia. Curabitur ut purus tincidunt, iaculis elit a, eleifend augue. Phasellus blandit augue vel sollicitudin blandit.</p>

  <article class="post abs" style="left:152px;top:193px"><div class="thumb abs" role="img" aria-label="Calendar date beside a countertop kiosk"></div><h3 class="abs">Nullam nunc purus, pretium sed faucibus nec.</h3><p class="abs">Nunc purus orci, adipiscig non ipsum non, pellentesque fringilla sapien.</p></article>
  <article class="post abs" style="left:462px;top:193px"><div class="thumb abs" role="img" aria-label="Calendar date beside a countertop kiosk"></div><h3 class="abs">Nullam nunc purus, pretium sed faucibus nec.</h3><p class="abs">Nunc purus orci, adipiscig non ipsum non, pellentesque fringilla sapien.</p></article>
  <article class="post abs" style="left:764px;top:193px"><div class="thumb abs" role="img" aria-label="Calendar date beside a countertop kiosk"></div><h3 class="abs">Nullam nunc purus, pretium sed faucibus nec.</h3><p class="abs">Nunc purus orci, adipiscig non ipsum non, pellentesque fringilla sapien.</p></article>
  <article class="post abs" style="left:152px;top:365px"><div class="thumb abs" role="img" aria-label="Calendar date beside a countertop kiosk"></div><h3 class="abs">Nullam nunc purus, pretium sed faucibus nec.</h3><p class="abs">Nunc purus orci, adipiscig non ipsum non, pellentesque fringilla sapien.</p></article>
  <article class="post abs" style="left:462px;top:365px"><div class="thumb abs" role="img" aria-label="Calendar date beside a countertop kiosk"></div><h3 class="abs">Nullam nunc purus, pretium sed faucibus nec.</h3><p class="abs">Nunc purus orci, adipiscig non ipsum non, pellentesque fringilla sapien.</p></article>
  <article class="post abs" style="left:764px;top:365px"><div class="thumb abs" role="img" aria-label="Calendar date beside a countertop kiosk"></div><h3 class="abs">Nullam nunc purus, pretium sed faucibus nec.</h3><p class="abs">Nunc purus orci, adipiscig non ipsum non, pellentesque fringilla sapien.</p></article>
</section>

<footer class="footer">
  <nav class="abs"><span>Services</span><span>Products</span><span>Leasing</span><span>Company</span><span>Case Studies</span><span>Sitemap</span></nav>
  <span class="social abs" style="left:945px" aria-label="Social profile"></span>
  <span class="social abs" style="left:976px" aria-label="Social profile"></span>
  <span class="social abs" style="left:1007px" aria-label="Social profile"></span>
</footer>

</body>
</html>
```